BBQ Catering & Pop-up Restaurant

I'm a catering company and a pop-up restaurant and need a website that will have the following at minimum (I'm open to suggestions): about me section, menu section, events section, a pre-order page. Here is an example of a site that I really like ... https://hollowcreeksmokehouse.example/ . I want to have a pre-order page where people can place orders online and the ability to take credit card payments. I've included a word doc with a draft write up to get started.
Updates

Reason: I am awaiting feedback from my partner and will be in touch ASAP.

Target Market(s)

BBQ Lovers

Industry/Entity Type

Caterer

Font styles to use
Serif
Other font styles liked:
• we can use multiple fonts where appropriate. I also like a faded, woody type font - which reminds me of the old western movies

Colors

Designer to choose colors to be used in the design.

Requirements
Must have
• I want
• - a smokey, woody, bbq type feel to the site.
• - my logo to be utilized
• - colors I like should compliment the colors in my logo
• - link to sign up for a news letter/ mailing list and something on the back end to capture data
Nice to have
• NA
Should not have
• NA

```html
<!DOCTYPE html>
<html lang="en">
<head>
<meta charset="utf-8">
<title>Emberline Smokehouse – BBQ Catering &amp; Pop-up Restaurant</title>
<link href="https://fonts.googleapis.com/css2?family=Bowlby+One&family=Libre+Baskerville&family=Open+Sans:wght@400;600;700&display=swap" rel="stylesheet">
<style>
:root{
  --red:#b3231a;
  --red-dark:#8f1a13;
  --ink:#231d1b;
  --night:#0d0b0a;
  --cream:#f7f3e6;
  --paper:#f1f0ee;
  --gold:#e8b321;
  --white:#ffffff;
  --muted:#8c8682;
  --line:#3e3532;
}
*{box-sizing:border-box;margin:0;padding:0}
html,body{width:1200px;height:4091px;overflow:hidden}
body{font-family:"Open Sans",sans-serif;color:var(--ink);background:var(--white);position:relative}
section,header,footer{position:relative;width:1200px;overflow:hidden}
.display{font-family:"Bowlby One",sans-serif;letter-spacing:1px;line-height:1.1}
.accent{color:var(--red)}
.btn{display:inline-block;background:var(--red);color:var(--white);font-size:12px;font-weight:700;text-transform:uppercase;border-radius:22px;padding:13px 34px;letter-spacing:.5px;text-decoration:none}
.photo{position:absolute}

/* hero */
.hero{height:633px;background:radial-gradient(ellipse at 70% 40%,#5a3a2a 0%,#2a1c16 55%,#120c0a 100%)}
.hero .photo{inset:0;background:linear-gradient(120deg,rgba(80,50,35,.4),rgba(20,12,10,.2))}
.nav{position:absolute;top:22px;left:0;width:100%;display:flex;justify-content:center;gap:40px}
.nav a{color:var(--white);font-size:13px;text-decoration:none;font-weight:600}
.brand{position:absolute;left:0;width:100%;top:210px;text-align:center}
.brand-name{font-family:"Bowlby One",sans-serif;color:var(--white);font-size:40px;letter-spacing:2px}
.hero-text{position:absolute;top:345px;left:240px;width:720px;text-align:center;color:#e9e2dc;font-size:13.5px;line-height:1.75}
.hero .btn{position:absolute;top:447px;left:510px;width:180px;text-align:center;padding:13px 0}

/* welcome */
.welcome{height:643px;background:var(--white)}
.welcome h2{position:absolute;top:44px;width:100%;text-align:center;font-size:38px}
.greens{position:absolute;right:0;top:0;width:220px;height:400px;background:linear-gradient(160deg,#d9e8b8 0%,#7fb14a 45%,rgba(255,255,255,0) 80%);border-bottom-left-radius:160px}
.service{position:absolute;top:196px;width:308px;height:376px;background:linear-gradient(180deg,#3a2a22,#1c1410 70%);}
.service .label{position:absolute;top:165px;width:100%;text-align:center;color:var(--gold);font-family:"Bowlby One",sans-serif;font-size:24px}
.service svg.icon{position:absolute;top:120px;left:139px}
.service .tab{position:absolute;bottom:-30px;left:124px;width:60px;height:60px;border-radius:50%;background:var(--white)}
.service .tab svg{position:absolute;left:22px;top:10px}

/* preorder */
.preorder{height:270px;background:var(--paper)}
.preorder p{position:absolute;top:64px;left:180px;width:840px;text-align:center;font-size:12.5px;line-height:1.7;color:#514a46}
.preorder .btn{position:absolute;top:138px;left:510px;width:180px;text-align:center;padding:13px 0}
.bowl{left:-30px;top:140px;width:300px;height:200px;border-radius:50%;background:radial-gradient(circle,#c98a4a 0%,#e6d2b5 55%,#f5f2ee 75%)}

/* menu */
.menu{height:799px;background:radial-gradient(ellipse at center,#2f2624,#1e1816)}
.menu h2{position:absolute;top:40px;width:100%;text-align:center;font-size:38px;color:var(--white)}
.menu .intro{position:absolute;top:104px;left:180px;width:840px;text-align:center;font-size:12.5px;line-height:1.7;color:var(--muted)}
.tabs{position:absolute;top:189px;left:172px;width:856px;height:66px;background:var(--red);display:flex}
.tabs li{list-style:none;flex:1;text-align:center;color:var(--white);font-size:12px;font-weight:700;padding-top:40px;position:relative}
.tabs li::before{content:"";position:absolute;top:14px;left:50%;margin-left:-10px;width:20px;height:18px;border-radius:10px 10px 3px 3px;background:var(--white)}
.tabs li.active{background:var(--white);color:var(--ink)}
.tabs li.active::before{background:var(--ink)}
.panel{position:absolute;top:255px;left:172px;width:856px;height:445px;border:1px solid var(--line);border-top:none}
.panel h3{position:absolute;top:30px;width:100%;text-align:center;font-family:"Libre Baskerville",serif;color:var(--white);font-size:20px;font-weight:400}
.panel h3::after{content:"";display:block;width:46px;height:1px;background:var(--muted);margin:14px auto 0}
.dish{position:absolute;width:380px;height:80px}
.dish .thumb{position:absolute;left:0;top:0;width:86px;height:62px;background:linear-gradient(135deg,#7a2a1a,#d8c7b4)}
.dish h4{position:absolute;left:100px;top:0;color:var(--white);font-size:13px;font-weight:600}
.dish p{position:absolute;left:100px;top:22px;width:260px;color:var(--muted);font-size:11.5px;line-height:1.55}
.plate{right:-40px;top:560px;width:310px;height:250px;border-radius:50%;background:radial-gradient(circle,#d49a52 0%,#efe4d2 55%,rgba(255,255,255,0) 72%)}

/* events */
.events{height:647px;background:var(--cream)}
.events h2{position:absolute;top:70px;width:100%;text-align:center;font-size:38px}
.pepper{left:-20px;top:-20px;width:200px;height:180px;border-radius:50%;background:radial-gradient(circle,#8a3a22 0%,#b98a5a 45%,rgba(247,243,230,0) 72%)}
.grid{position:absolute;top:161px;left:112px;width:976px;display:grid;grid-template-columns:repeat(4,244px);grid-auto-rows:206px}
.cell-photo{background:linear-gradient(135deg,#5b3a24,#a97a4e)}
.cell-photo.green{background:linear-gradient(135deg,#355a2a,#c7d9a0)}
.cell-photo.dark{background:linear-gradient(135deg,#2c2420,#8c5a34)}
.cell-text{background:var(--white);text-align:center;padding-top:40px}
.cell-text h4{font-family:"Libre Baskerville",serif;font-weight:400;font-size:15px}
.cell-text time{display:block;font-family:"Libre Baskerville",serif;font-size:11px;color:var(--muted);margin-top:6px}
.cell-text .rule{width:120px;height:1px;background:#ddd;margin:14px auto;position:relative}
.cell-text .rule::after{content:"";position:absolute;left:56px;top:-4px;width:8px;height:8px;border-radius:50%;background:#ccc}
.cell-text p{font-size:11.5px;line-height:1.6;color:#514a46;padding:0 36px}

/* newsletter */
.newsletter{height:281px;background:var(--night)}
.newsletter h2{position:absolute;top:46px;width:100%;text-align:center;font-size:36px;color:var(--white)}
.newsletter p{position:absolute;top:104px;left:180px;width:840px;text-align:center;font-size:12px;line-height:1.7;color:#5e5854}
.signup{position:absolute;top:178px;left:338px;display:flex;gap:8px}
.signup .field{width:352px;height:38px;border-radius:19px;background:#e8e8e8;color:#9a9a9a;font-size:11px;padding:11px 20px}
.signup .btn{height:38px;width:164px;text-align:center;padding:11px 0}

/* testimonial */
.testimonial{height:403px;background:var(--white)}
.napkin{right:120px;top:0;width:200px;height:80px;background:linear-gradient(160deg,#e6e6e6 0%,#c6323a 55%,#f5d6d6 100%);clip-path:polygon(0 0,100% 0,70% 100%)}
.avatar{left:530px;top:58px;width:140px;height:140px;border-radius:50%;background:radial-gradient(circle at 50% 40%,#c79a7a,#5a3b2a);border:4px solid #eee}
.testimonial blockquote{position:absolute;top:218px;left:180px;width:840px;text-align:center;font-size:12.5px;line-height:1.75;color:#514a46}
.dots{position:absolute;top:326px;left:570px;display:flex;gap:10px}
.dots i{width:12px;height:12px;border-radius:50%;background:#c9c9c9}
.dots i:first-child{background:var(--red)}

/* footer */
.site-footer{height:415px;background:linear-gradient(180deg,#1b1412,#0f0b0a)}
.foot-brand{position:absolute;left:112px;top:120px;font-family:"Bowlby One",sans-serif;font-size:32px;color:var(--white);letter-spacing:1px}
.col{position:absolute;top:102px;color:var(--white)}
.col h5{font-size:17px;font-weight:600;margin-bottom:14px}
.col h6{font-size:12px;font-weight:600;margin-bottom:4px}
.col p{font-size:11.5px;line-height:1.55;color:#c9c2bd;margin-bottom:10px}
.icons{display:flex;gap:10px}
.icons i{width:14px;height:14px;border-radius:50%;background:var(--white)}
.cards{display:flex;gap:6px}
.cards i{width:40px;height:24px;border-radius:3px;background:#d9d9d9}
.copyright{position:absolute;top:324px;width:100%;text-align:center;font-size:11px;color:#9a928d}
</style>
</head>
<body>

<header class="hero">
  <div class="photo" role="img" aria-label="Plated smoked meat with asparagus on a restaurant table"></div>
  <nav class="nav">
    <a href="#">HOME</a><a href="#">ABOUT US</a><a href="#">OUR MENU</a><a href="#">EVENTS</a><a href="#">PREORDERS</a>
  </nav>
  <div class="brand"><span class="brand-name">EMBERLINE SMOKEHOUSE</span></div>
  <p class="hero-text">Contrary to popular belief, Lorem Ipsum is not simply random text. It has roots in a piece of classical Latin literature from 45 BC, making it over 2000 years old. Alder Quinn, a Latin professor at Brookfield College in Oregon, looked up one of the more obscure Latin words, consectetur.</p>
  <a class="btn" href="#">Book your place</a>
</header>

<section class="welcome">
  <div class="greens" role="img" aria-label="Fresh salad leaves falling"></div>
  <h2 class="display">WELCOME TO THE BEST<br><span class="accent">CATERING COMPANY</span></h2>

  <article class="service" style="left:112px" role="img" aria-label="Catering buffet spread">
    <svg class="icon" width="30" height="36" viewBox="0 0 30 36"><path d="M3 22h24a12 12 0 0 0-24 0z" fill="#e8b321"/><rect x="1" y="24" width="28" height="4" fill="#e8b321"/></svg>
    <div class="label">CATERING</div>
    <div class="tab"><svg width="16" height="10" viewBox="0 0 16 10"><path d="M2 2l6 6 6-6" stroke="#231d1b" stroke-width="2" fill="none"/></svg></div>
  </article>
  <article class="service" style="left:446px" role="img" aria-label="Event table with wine glasses">
    <svg class="icon" width="30" height="36" viewBox="0 0 30 36"><path d="M4 4h22l-11 14z" fill="#e8b321"/><rect x="14" y="18" width="2" height="12" fill="#e8b321"/><rect x="8" y="30" width="14" height="3" fill="#e8b321"/></svg>
    <div class="label">EVENTS</div>
    <div class="tab"><svg width="16" height="10" viewBox="0 0 16 10"><path d="M2 2l6 6 6-6" stroke="#231d1b" stroke-width="2" fill="none"/></svg></div>
  </article>
  <article class="service" style="left:780px" role="img" aria-label="Plated dish from the menu">
    <svg class="icon" width="30" height="36" viewBox="0 0 30 36"><rect x="4" y="4" width="22" height="28" fill="#e8b321"/><rect x="9" y="10" width="12" height="2" fill="#3a2a22"/><rect x="9" y="16" width="12" height="2" fill="#3a2a22"/></svg>
    <div class="label">MENU</div>
    <div class="tab"><svg width="16" height="10" viewBox="0 0 16 10"><path d="M2 2l6 6 6-6" stroke="#231d1b" stroke-width="2" fill="none"/></svg></div>
  </article>
</section>

<section class="preorder">
  <div class="photo bowl" role="img" aria-label="Bowl of pasta with herbs"></div>
  <p>Contrary to popular belief, Lorem Ipsum is not simply random text. It has roots in a piece of classical Latin literature from 45 BC, making it over 2000 years old. Alder Quinn, a Latin professor at Brookfield College in Oregon, looked up one of the.</p>
  <a class="btn" href="#">Preorders</a>
</section>

<section class="menu">
  <h2 class="display">OUR <span class="accent">MENU</span></h2>
  <p class="intro">Contrary to popular belief, Lorem Ipsum is not simply random text. It has roots in a piece of classical Latin literature from 45 BC, making it over 2000 years old. Alder Quinn, a Latin professor at Brookfield College in Oregon.</p>
  <ul class="tabs">
    <li>STARTER</li><li class="active">MAIN</li><li>BUFFET</li><li>FASTFOOD</li><li>DESSERTS</li><li>DRINKS</li>
  </ul>
  <div class="panel">
    <h3>Main Course</h3>
    <div class="dish" style="left:19px;top:121px"><div class="thumb" role="img" aria-label="Chilli beef dish"></div><h4>Maxican Chilli Beef</h4><p>Contrary to popular belief, Lorem Ipsum is not simply random text. It has roots in a piece</p></div>
    <div class="dish" style="left:450px;top:121px"><div class="thumb" role="img" aria-label="Chilli beef dish"></div><h4>Maxican Chilli Beef</h4><p>Contrary to popular belief, Lorem Ipsum is not simply random text. It has roots in a piece</p></div>
    <div class="dish" style="left:19px;top:225px"><div class="thumb" role="img" aria-label="Chilli beef dish"></div><h4>Maxican Chilli Beef</h4><p>Contrary to popular belief, Lorem Ipsum is not simply random text. It has roots in a piece</p></div>
    <div class="dish" style="left:450px;top:225px"><div class="thumb" role="img" aria-label="Chilli beef dish"></div><h4>Maxican Chilli Beef</h4><p>Contrary to popular belief, Lorem Ipsum is not simply random text. It has roots in a piece</p></div>
    <div class="dish" style="left:19px;top:331px"><div class="thumb" role="img" aria-label="Chilli beef dish"></div><h4>Maxican Chilli Beef</h4><p>Contrary to popular belief, Lorem Ipsum is not simply random text. It has roots in a piece</p></div>
    <div class="dish" style="left:450px;top:331px"><div class="thumb" role="img" aria-label="Chilli beef dish"></div><h4>Maxican Chilli Beef</h4><p>Contrary to popular belief, Lorem Ipsum is not simply random text. It has roots in a piece</p></div>
  </div>
  <div class="photo plate" role="img" aria-label="Plate of noodles with salad garnish"></div>
</section>

<section class="events">
  <div class="photo pepper" role="img" aria-label="Scattered peppercorns"></div>
  <h2 class="display">LATEST <span class="accent">EVENTS</span></h2>
  <div class="grid">
    <div class="cell-photo" role="img" aria-label="Roasted chicken pieces"></div>
    <div class="cell-text"><h4>New York Strip Steak</h4><time>29 July, 2014</time><div class="rule"></div><p>Lorem ipsum dolor sit amet, cone ectetur adipiscing elit.</p></div>
    <div class="cell-photo dark" role="img" aria-label="Noodle bowl with chopsticks"></div>
    <div class="cell-text"><h4>New York Strip Steak</h4><time>29 July, 2014</time><div class="rule"></div><p>Lorem ipsum dolor sit amet, cone ectetur adipiscing elit.</p></div>
    <div class="cell-text"><h4>New York Strip Steak</h4><time>29 July, 2014</time><div class="rule"></div><p>Lorem ipsum dolor sit amet, cone ectetur adipiscing elit.</p></div>
    <div class="cell-photo" role="img" aria-label="Stuffed flatbread wrap"></div>
    <div class="cell-text"><h4>New York Strip Steak</h4><time>29 July, 2014</time><div class="rule"></div><p>Lorem ipsum dolor sit amet, cone ectetur adipiscing elit.</p></div>
    <div class="cell-photo green" role="img" aria-label="Bowl of sliced leeks"></div>
  </div>
</section>

<section class="newsletter">
  <h2 class="display">NEWSLETTER <span class="accent">SIGNUP</span></h2>
  <p>Contrary to popular belief, Lorem Ipsum is not simply random text. It has roots in a piece of classical Latin literature from 45 BC, making it over 2000 years old. Alder Quinn, a Latin professor at Brookfield College in Oregon, looked up one of the.</p>
  <div class="signup"><div class="field">Enter Name</div><a class="btn" href="#">Subscribe</a></div>
</section>

<section class="testimonial">
  <div class="photo napkin" role="img" aria-label="Plate on a checkered napkin"></div>
  <div class="photo avatar" role="img" aria-label="Portrait of a happy customer"></div>
  <blockquote>Contrary to popular belief, Lorem Ipsum is not simply random text. It has roots in a piece of classical Latin literature from 45 BC, making it over 2000 years old. Alder Quinn, a Latin professor at Brookfield College in Oregon, looked up one of the. Contrary to popular belief, Lorem Ipsum is not simply random text. It has roots in a piece of classical Latin literature from 45 BC, making it over 2000 years old. Alder Quinn, a Latin professor at Brookfield College in Oregon, looked up one of the.</blockquote>
  <div class="dots"><i></i><i></i><i></i><i></i></div>
</section>

<footer class="site-footer">
  <div class="foot-brand">EMBERLINE</div>
  <div class="col" style="left:491px">
    <h5>Contact Us</h5>
    <h6>Address</h6>
    <p>Cedar Row Depot, Unit 12, No.: 88<br>Old Mill Lane, Ridgeford 40912</p>
    <h6>Join Us</h6>
    <div class="icons"><i></i><i></i><i></i></div>
  </div>
  <div class="col" style="left:927px">
    <h5>We are open</h5>
    <h6>Opening Hours</h6>
    <p>All Day 9:00 AM to 11:00 PM</p>
    <h6>We Accept</h6>
    <div class="cards"><i></i><i></i><i></i><i></i></div>
  </div>
  <div class="copyright">copyrights © All Rights Reserved 2017</div>
</footer>

</body>
</html>
```